Business Card Needed for Crafter of Pottery, Jewelry and Artwork

Calling all designers in search of an artistic challenge.

I need a new business card design for my pottery, jewelry and artwork business, Woven Glass and Tide, based in Vancouver BC.

I would like a card that is bright and inviting and preferably incorporates my logo and a sample of photos of my work while having a clean fresh look. The following contact details would preferably be included on the card as well:
• Helena Pikeworth
• Designer
• Phone: 604.555.0172
• Email: Designer@WovenGlassandTide.example
• Website: www.WovenGlassandTide.example
• Blog: www.ShapingHillside.example

The logo is attached in two color schemes in both Vector and Source formats. On past cards I’ve also included photos of my work. By including photos of the work the pieces are showcased and it catches people’s eye and prompts them to pick up the card and look at it more closely. For example, if I leave a stack in a coffee shop I want people to be drawn to the card, to pick it up and get a sense of the my product lines. Please feel free to pull photos of my work directly off of my website. If you need photos with higher pixels please let me know and I’ll email them directly to you. The website background is bffbda (191, 251, 218). I would like the business cards to match the feel of the website for consistency but the cards do not need to use the exact same colors. My website and current business card are predominantly turquoise shades. The background uses stripes provided by the website template. I don’t know the exact colors of the stripes.

My current business card is attached to show the use of photos in a design. Please note that I am not thrilled with my own design and am looking for variations and completely new designs. This example is not meant to be used as a template or starting point.

Here is some background surrounding my company:
WGT offers one of a kind jewelry, pottery, artwork and leather bags each designed with a twist. The pottery varies from rustic every day functional ware to raku artwork. The jewelry ranges from simple sterling every day pieces to multimedia pieces incorporating stone, metal, ceramics and fabric. The artwork is multimedia, typically acrylic paired with a natural element such as bark. All the bags are leather with reworked kimono fabric or patterned silk lining.

Feel free to check out my website to get a flavour for my work and the color scheme I've used on marketing materials so far. www.wovenglassandtide.example
Updates

Thank you to everyone who has submitted a design so far. I hope everyone has received some helpful feedback.

I'm going to post a survey to customers and friends asking for their votes. If you have new designs to submit please try to get them in by Saturday March 30 at noon so that I can include it in the survey launch.

Thank you

Target Market(s)

Females aged 25-65 interested in one of a kind functional pottery and jewelry.

Industry/Entity Type

Coffee Shop

Requirements
Must have
• Contact information, website, blog
Nice to have
• Logo, photos

```html
<!DOCTYPE html>
<html lang="en">
<head>
<meta charset="utf-8">
<title>Woven Glass and Tide – Business Card</title>
<link href="https://fonts.googleapis.com/css2?family=Questrial&display=swap" rel="stylesheet">
<style>
  :root {
    --stage: #e9ebee;
    --navy: #241f66;
    --navy-soft: #3a3584;
    --turquoise: #56c2bb;
    --white: #ffffff;
    --text-light: #f2f1fb;
    --photo-celadon: #b9d6cc;
    --photo-cream: #d8cbb4;
    --photo-cobalt: #2e4f93;
    --shadow: rgba(20, 24, 40, 0.22);
  }
  * { box-sizing: border-box; margin: 0; padding: 0; }
  html, body {
    width: 1200px;
    height: 1200px;
    overflow: hidden;
    background: var(--stage);
    font-family: "Questrial", "Century Gothic", sans-serif;
  }
  .canvas {
    width: 1200px;
    height: 1200px;
    display: flex;
    flex-direction: column;
    align-items: center;
    justify-content: center;
    gap: 60px;
  }
  .card {
    width: 840px;
    height: 480px;
    box-shadow: 0 12px 30px var(--shadow);
    overflow: hidden;
    position: relative;
  }

  /* Back: contact side */
  .card-back {
    display: flex;
    background: var(--navy);
  }
  .contact-panel {
    flex: 0 0 72%;
    position: relative;
    color: var(--text-light);
    padding: 44px 0 0 0;
  }
  .dot-field {
    position: absolute;
    inset: 0;
    background:
      radial-gradient(ellipse at 35% 8%, rgba(120, 118, 190, 0.35), transparent 45%),
      radial-gradient(ellipse at 80% 92%, rgba(120, 118, 190, 0.35), transparent 45%);
  }
  .brand-title {
    position: relative;
    font-size: 38px;
    font-weight: 400;
    letter-spacing: 0.5px;
    padding-left: 36px;
  }
  .title-rule {
    position: relative;
    height: 2px;
    background: var(--text-light);
    opacity: 0.85;
    margin: 14px 0 26px 0;
    width: 100%;
  }
  .holder {
    position: relative;
    font-size: 27px;
    padding-left: 36px;
    margin-bottom: 48px;
  }
  .holder .role { font-style: italic; opacity: 0.95; }
  .contact-list {
    position: relative;
    list-style: none;
    padding-left: 36px;
    font-size: 22px;
    line-height: 1.42;
  }
  .photo-strip {
    flex: 1;
    display: flex;
    flex-direction: column;
  }
  .photo { flex: 1; }
  .photo-bowl { background: linear-gradient(160deg, var(--photo-celadon), var(--photo-cream)); }
  .photo-vase { background: radial-gradient(ellipse at 50% 55%, #4f72b8, var(--photo-cobalt) 60%, #6b5a4a); }
  .photo-jewelry { background: linear-gradient(180deg, #e7e4dc, #7fb7ae); }

  /* Front: name side */
  .card-front {
    background: var(--turquoise);
    display: flex;
    flex-direction: column;
    align-items: center;
    justify-content: center;
    gap: 26px;
  }
  .brand-circle {
    width: 150px;
    height: 150px;
    border-radius: 50%;
    background: var(--white);
  }
  .brand-name {
    font-size: 44px;
    color: var(--white);
    letter-spacing: 1px;
  }
</style>
</head>
<body>
  <main class="canvas">
    <section class="card card-back" aria-label="Business card, contact side">
      <div class="contact-panel">
        <div class="dot-field" role="img" aria-label="Soft scattered circle pattern in lavender tones"></div>
        <h1 class="brand-title">-Woven Glass and Tide-</h1>
        <div class="title-rule"></div>
        <p class="holder">-Helena Pikeworth/ <span class="role">Designer</span></p>
        <ul class="contact-list">
          <li>-Phone: 604.555.0172</li>
          <li>-Email: Designer@WovenGlassandTide.example</li>
          <li>-Website: www.WovenGlassandTide.example</li>
          <li>-Blog: www.ShapingHillside.example</li>
        </ul>
      </div>
      <div class="photo-strip">
        <div class="photo photo-bowl" role="img" aria-label="Photo of celadon glazed pottery dishes"></div>
        <div class="photo photo-vase" role="img" aria-label="Photo of a cobalt blue glazed vase"></div>
        <div class="photo photo-jewelry" role="img" aria-label="Photo of handmade turquoise bead jewelry"></div>
      </div>
    </section>

    <section class="card card-front" aria-label="Business card, brand side">
      <div class="brand-circle"></div>
      <p class="brand-name">Woven Glass and Tide</p>
    </section>
  </main>
</body>
</html>
```